Harbourline Advisory Group Wordpress Design

See attached brief. If you have questions beyond this please let me know. Brief document is HA Group Website Design v1. Other documents are files from logo creation and business cards to give you an idea of colours and images. Also see document that shows examples of the types of images I want to display on the website.

Focus of site is for customers and to drive traffic from social media etc. Company is startup consulting business in Customer Experience and Contact Centre. We offer benchmarking, strategy reviews, technology audits. etc

Looking for the site to use the existing Wordpress theme on Nestora or something compatible. Happy to change if there is a good reason for doing so.

Has to be easy to manage ongoing if possible.

Target Market(s)

HAG is a consulting organisation in contact centre and customer experience

Number of Pages Required

4 page

Font styles to use
Serif
Sans Serif

Colors
0255a3
3276b5
33a6d7
0293ce
ffffff
fefdec

Requirements
Must have
• Hosted on Nestora so must be compatible. Preference is to use the theme that is already there (Lumeo) unless there is a reason not to
Nice to have
• see brief

```html
<!DOCTYPE html>
<html lang="en">
<head>
<meta charset="utf-8">
<title>Harbourline Advisory Group</title>
<link href="https://fonts.googleapis.com/css2?family=Oswald:wght@300;400;500;700&family=PT+Sans:wght@400;700&family=Open+Sans:wght@400;600;700&display=swap" rel="stylesheet">
<style>
:root{
  --blue:#19a6ee;
  --blue-dark:#0255a3;
  --blue-mid:#3276b5;
  --blue-soft:#33a6d7;
  --ink:#2d2d2d;
  --grey:#6d6d6d;
  --line:#e2e2e2;
  --white:#ffffff;
  --cream:#fefdec;
}
*{margin:0;padding:0;box-sizing:border-box}
html,body{width:1200px;height:3905px;overflow:hidden}
body{position:relative;background:var(--white);font-family:"Open Sans",sans-serif;color:var(--ink)}
.img{position:absolute;display:block}

/* header */
.site-header{position:absolute;left:0;top:0;width:1200px;height:86px;background:var(--white)}
.brand{position:absolute;left:99px;top:12px;display:flex;align-items:center;gap:10px}
.brand-mark{width:24px;height:24px;border-radius:50%;background:var(--blue)}
.brand-name{font-family:"Oswald",sans-serif;font-weight:700;font-size:30px;color:var(--blue-dark);line-height:1}
.brand-sub{position:absolute;left:99px;top:52px;font-family:"Oswald",sans-serif;font-size:10px;letter-spacing:1.5px;color:var(--blue-dark);text-transform:uppercase}
.main-nav{position:absolute;left:658px;top:33px;display:flex;gap:23px;font-family:"PT Sans",sans-serif;font-size:14px;color:#444}
.search-btn{position:absolute;left:1041px;top:21px;width:60px;height:44px;background:var(--blue)}

/* hero */
.hero{position:absolute;left:0;top:86px;width:1200px;height:531px;overflow:hidden}
.hero-photo{left:0;top:0;width:1200px;height:531px;background:linear-gradient(100deg,#6c7277 0%,#9aa0a2 30%,#c9c3b9 55%,#8a7f74 75%,#b7b3ae 100%)}
.hero-t1{position:absolute;left:96px;top:95px;font-family:"Oswald",sans-serif;font-weight:300;font-size:92px;line-height:100px;color:var(--white)}
.hero-t2{position:absolute;left:96px;top:193px;font-family:"Oswald",sans-serif;font-weight:700;font-size:102px;line-height:108px;color:var(--white)}
.hero-t3{position:absolute;left:96px;top:296px;font-family:"Oswald",sans-serif;font-weight:400;font-size:54px;line-height:60px;color:var(--white)}
.btn-ghost{position:absolute;left:99px;top:383px;width:177px;height:54px;border:2px solid var(--white);color:var(--white);font-family:"Oswald",sans-serif;font-size:17px;display:flex;align-items:center;justify-content:center}
.hero-arrow{position:absolute;top:239px;width:52px;height:52px;background:rgba(40,40,40,.8)}
.hero-thumb{position:absolute;left:1096px;top:239px;width:52px;height:52px;background:#b6aaa0}
.hero-next{position:absolute;left:1148px;top:239px;width:52px;height:52px;background:var(--blue)}
.hero-dots{position:absolute;left:503px;top:487px;display:flex;gap:10px}
.hero-dots span{width:55px;height:5px;background:rgba(255,255,255,.6)}
.hero-dots span.on{background:var(--blue)}
.side-social{position:absolute;left:1148px;top:547px}
.side-social span{display:block;width:52px;height:52px;margin-bottom:2px;background:var(--blue-mid)}
.side-social span+span{background:var(--blue)}

/* teasers */
.teaser{position:absolute;top:651px;width:310px;display:flex;gap:12px}
.thumb{width:109px;flex:0 0 109px;height:94px}
.teaser h4,.news-item h4{font-family:"PT Sans",sans-serif;font-weight:700;font-size:13px;color:var(--ink);margin-bottom:6px}
.teaser p,.news-item p{font-size:11px;line-height:15px;color:var(--grey)}

/* video + welcome */
.video{left:99px;top:781px;width:661px;height:273px;background:linear-gradient(180deg,#8d8c8d,#4b4b4e)}
.play{position:absolute;left:398px;top:882px;width:62px;height:42px;border-radius:8px;background:rgba(255,255,255,.85)}
.play::after{content:"";position:absolute;left:25px;top:12px;border-left:16px solid #555;border-top:9px solid transparent;border-bottom:9px solid transparent}
.play-label{position:absolute;left:372px;top:943px;font-family:"Oswald",sans-serif;font-size:11px;color:var(--blue)}
.video-title{position:absolute;left:122px;top:978px;font-family:"Oswald",sans-serif;font-size:21px;line-height:27px;color:var(--white);text-transform:uppercase}
.welcome-h{position:absolute;left:99px;top:1074px;font-family:"Oswald",sans-serif;font-weight:500;font-size:31px;color:var(--ink)}
.welcome-h em{font-style:normal;color:var(--blue)}
.welcome-sub{position:absolute;left:99px;top:1120px;font-family:"Oswald",sans-serif;font-weight:300;font-size:25px;color:var(--ink)}
.welcome-p{position:absolute;left:99px;top:1163px;width:660px;font-size:11.5px;line-height:17px;color:var(--grey)}
.btn-solid{position:absolute;width:177px;height:55px;background:var(--blue);color:var(--white);font-family:"Oswald",sans-serif;font-size:17px;display:flex;align-items:center;justify-content:center}

/* news */
.news-h{position:absolute;left:781px;top:770px;font-family:"Oswald",sans-serif;font-weight:500;font-size:32px;color:var(--ink)}
.news-h em{font-style:normal;color:var(--blue)}
.news-item{position:absolute;left:781px;width:320px;display:flex;gap:14px}
.news-item .thumb{height:96px}

/* services */
.services{position:absolute;left:0;top:1354px;width:1200px;height:692px;background:var(--blue)}
.sec-title{position:absolute;left:0;width:1200px;text-align:center;font-family:"Oswald",sans-serif;font-weight:500;font-size:30px;color:var(--white)}
.circle{position:absolute;width:182px;height:182px;border-radius:50%;border:4px solid var(--white)}
.svc{position:absolute;width:290px;color:var(--white)}
.svc h3{font-family:"PT Sans",sans-serif;font-weight:700;font-size:22px;margin-bottom:20px}
.svc p{font-size:13px;line-height:22px}
.svc b{font-weight:700}
.svc.left{text-align:right}
.btn-white{position:absolute;left:510px;top:1939px;width:177px;height:52px;background:var(--white);color:var(--blue);font-family:"Oswald",sans-serif;font-size:15px;display:flex;align-items:center;justify-content:center}

/* blog */
.blog{position:absolute;left:0;top:2046px;width:1200px;height:643px;background:linear-gradient(180deg,#4d4f52,#3a3d41 60%,#55504a)}
.post{position:absolute;width:489px;height:188px;background:var(--white)}
.post .pic{position:absolute;top:0;width:255px;height:188px}
.post .body{position:absolute;top:18px;width:210px}
.post h4{font-family:"Oswald",sans-serif;font-size:17px;line-height:21px;color:var(--blue);text-transform:uppercase}
.post .meta{font-family:"Oswald",sans-serif;font-size:10px;line-height:13px;color:#555;margin-top:8px;text-transform:uppercase}
.post .meta span{color:var(--blue)}
.post .more{display:inline-block;margin-top:14px;padding:9px 12px;background:var(--blue);color:var(--white);font-family:"Oswald",sans-serif;font-size:11px}
.dots{position:absolute;display:flex;gap:6px}
.dots span{width:12px;height:12px;border-radius:50%;border:2px solid #bbb}
.dots span.on{background:var(--blue);border-color:var(--blue)}

/* partners */
.partner-logo{position:absolute;left:0;top:2740px;width:1200px;display:flex;justify-content:center;align-items:center;gap:14px}
.partner-logo .brand-mark{width:34px;height:34px}
.partner-logo .brand-name{font-size:66px}
.partner-tag{position:absolute;left:0;top:2855px;width:1200px;text-align:center;font-family:"Oswald",sans-serif;font-size:19px;letter-spacing:8px;color:var(--ink);text-transform:uppercase}
.client{position:absolute;width:200px;text-align:center;font-family:"Oswald",sans-serif;font-weight:500;font-size:30px;color:var(--blue-dark)}

/* contact */
.contact{position:absolute;left:0;top:3298px;width:1200px;height:607px;background:linear-gradient(180deg,#2f5f97,#1f4f86 60%,#284f7c)}
.contact-h3{position:absolute;font-family:"PT Sans",sans-serif;font-weight:700;font-size:15px;color:var(--white)}
.contact-p{position:absolute;left:99px;top:3472px;width:746px;font-size:11.5px;line-height:17px;color:#dfe8f3}
.field{position:absolute;height:32px;border:1px solid rgba(255,255,255,.7);color:var(--white);font-size:12px;padding:7px 10px}
.info{position:absolute;left:872px;top:3475px;font-family:"PT Sans",sans-serif;font-weight:700;font-size:12px;line-height:17px;color:var(--white)}
.social-grid{position:absolute;left:872px;top:3686px;display:grid;grid-template-columns:repeat(7,14px);gap:22px 20px}
.social-grid span{width:14px;height:14px;border-radius:50%;background:var(--white)}
.rule{position:absolute;left:872px;width:229px;height:1px;background:rgba(255,255,255,.4)}
.footer-line{position:absolute;left:0;top:3826px;width:1200px;height:1px;background:rgba(255,255,255,.3)}
.copyright{position:absolute;left:99px;top:3842px;font-size:11px;color:#dfe8f3}
</style>
</head>
<body>

<header class="site-header">
  <div class="brand"><span class="brand-mark"></span><span class="brand-name">HAG</span></div>
  <div class="brand-sub">Harbourline Advisory Group</div>
  <nav class="main-nav"><span>Home Page</span><span>Services</span><span>Partners</span><span>Blog</span><span>Get In Touch</span></nav>
  <div class="search-btn">
    <svg width="60" height="44" viewBox="0 0 60 44"><circle cx="29" cy="21" r="5" fill="none" stroke="#fff" stroke-width="2"/><line x1="33" y1="25" x2="37" y2="29" stroke="#fff" stroke-width="2"/></svg>
  </div>
</header>

<section class="hero">
  <div class="img hero-photo" role="img" aria-label="Smiling man in a checked shirt holding a coffee cup in an office"></div>
  <div class="hero-t1">CUSTOMER</div>
  <div class="hero-t2">EXPERIENCE</div>
  <div class="hero-t3">PARTNER</div>
  <div class="btn-ghost">READ MORE</div>
  <div class="hero-arrow" style="left:0">
    <svg width="52" height="52"><polyline points="30,18 22,26 30,34" fill="none" stroke="#fff" stroke-width="3"/></svg>
  </div>
  <div class="hero-thumb" role="img" aria-label="Next slide preview"></div>
  <div class="hero-next">
    <svg width="52" height="52"><polyline points="22,18 30,26 22,34" fill="none" stroke="#fff" stroke-width="3"/></svg>
  </div>
  <div class="hero-dots"><span></span><span class="on"></span><span></span></div>
</section>
<div class="side-social"><span></span><span></span></div>

<div class="teaser" style="left:99px">
  <div class="thumb img" style="position:static;background:linear-gradient(135deg,#c7c2bb,#6f7c88)" role="img" aria-label="Older couple reviewing paperwork"></div>
  <div><h4>LOREM IPSUM DUMMY TEXT</h4><p>Contrary to popular belief, Lorem Ipsum is not simply random text. It has roots in a piece of classical Latin literature from 45 BC...</p></div>
</div>
<div class="teaser" style="left:440px">
  <div class="thumb img" style="position:static;background:linear-gradient(135deg,#9a9a9a,#4a4a4a)" role="img" aria-label="Man working at a laptop"></div>
  <div><h4>LOREM IPSUM DUMMY TEXT</h4><p>Contrary to popular belief, Lorem Ipsum is not simply random text. It has roots in a piece of classical Latin literature from 45 BC...</p></div>
</div>
<div class="teaser" style="left:781px">
  <div class="thumb img" style="position:static;background:linear-gradient(135deg,#d8d5cf,#8a8f96)" role="img" aria-label="Man typing at a desk computer"></div>
  <div><h4>LOREM IPSUM DUMMY TEXT</h4><p>Contrary to popular belief, Lorem Ipsum is not simply random text. It has roots in a piece of classical Latin literature from 45 BC...</p></div>
</div>

<div class="img video" role="img" aria-label="Video still of a business team standing together"></div>
<div class="play"></div>
<div class="play-label">CLICK HERE TO PLAY</div>
<div class="video-title">Watch the<br>book trailer</div>

<h2 class="welcome-h">WELCOME TO <em>CUSTOMER EXPERIENCE</em></h2>
<div class="welcome-sub">LOREM IPSUM IS DUMMY TEXT USED FOR PRINTING</div>
<p class="welcome-p">Contrary to popular belief, Lorem Ipsum is not simply random text. It has roots in a piece of classical Latin literature from 45 BC, making it over 2000 years old. Daniel Orwell, a Latin professor at Westbrook College, looked up one of the more obscure Latin words, consectetur, from a Lorem Ipsum passage, and going through the cites of the word in classical literature, discovered the undoubtable source.</p>
<div class="btn-solid" style="left:99px;top:1257px">READ MORE</div>

<h2 class="news-h">NEWS &amp; <em>EVENTS</em></h2>
<div class="news-item" style="top:833px">
  <div class="thumb img" style="position:static;background:linear-gradient(135deg,#d6d3cd,#7f8790)" role="img" aria-label="Man at a desk computer"></div>
  <div><h4>LOREM IPSUM DUMMY TEXT</h4><p>Contrary to popular belief, Lorem Ipsum is not simply random text. It has roots in a piece of classical Latin literature from 45 BC...</p></div>
</div>
<div class="news-item" style="top:963px">
  <div class="thumb img" style="position:static;background:linear-gradient(135deg,#9c9c9c,#454545)" role="img" aria-label="Man working at a laptop"></div>
  <div><h4>LOREM IPSUM DUMMY TEXT</h4><p>Contrary to popular belief, Lorem Ipsum is not simply random text. It has roots in a piece of classical Latin literature from 45 BC...</p></div>
</div>
<div class="news-item" style="top:1093px">
  <div class="thumb img" style="position:static;background:linear-gradient(135deg,#c5c0b8,#6e7b87)" role="img" aria-label="Older couple reviewing paperwork"></div>
  <div><h4>LOREM IPSUM DUMMY TEXT</h4><p>Contrary to popular belief, Lorem Ipsum is not simply random text. It has roots in a piece of classical Latin literature from 45 BC...</p></div>
</div>
<div class="news-item" style="top:1223px">
  <div class="thumb img" style="position:static;background:linear-gradient(135deg,#d6d3cd,#7f8790)" role="img" aria-label="Man at a desk computer"></div>
  <div><h4>LOREM IPSUM DUMMY TEXT</h4><p>Contrary to popular belief, Lorem Ipsum is not simply random text. It has roots in a piece of classical Latin literature from 45 BC...</p></div>
</div>

<section class="services">
  <h2 class="sec-title" style="top:46px">OUR SERVICES</h2>
</section>
<div class="circle img" style="left:414px;top:1484px;background:linear-gradient(135deg,#e9e6e2,#9b8d80)" role="img" aria-label="Support agent wearing a headset"></div>
<div class="circle img" style="left:622px;top:1484px;background:linear-gradient(135deg,#f2f2f2,#b5b5b5)" role="img" aria-label="Pair of glasses"></div>
<div class="circle img" style="left:414px;top:1695px;background:linear-gradient(135deg,#f0f0f0,#8a8a8a)" role="img" aria-label="Colleagues working together at a desk"></div>
<div class="circle img" style="left:622px;top:1695px;background:linear-gradient(135deg,#6f6f6f,#262626)" role="img" aria-label="Business handshake"></div>
<div class="svc left" style="left:98px;top:1514px"><h3>Service 01</h3><p>Donec consectetuer ligula vulputate sem tristique cursus. Nam nulla quam, gravida non, comm lorem ipin <b>read more ...</b></p></div>
<div class="svc" style="left:828px;top:1514px"><h3>Service 02</h3><p>Lorem ipsum dolor sit amet, consectetuer adipiscing elit. Donec odio. Quisque volutpat matti <b>read more ...</b></p></div>
<div class="svc left" style="left:98px;top:1724px"><h3>Service 03</h3><p>Donec consectetuer ligula vulputate sem tristique cursus. Nam nulla quam, gravida non, comm lorem ipin <b>read more ...</b></p></div>
<div class="svc" style="left:828px;top:1724px"><h3>Service 04</h3><p>Lorem ipsum dolor sit amet, consectetuer adipiscing elit. Donec odio. Quisque volutpat matti <b>read more ...</b></p></div>
<div class="btn-white">VIEW MORE SERVICES</div>

<section class="blog" role="img" aria-label="Blurred city street background">
  <h2 class="sec-title" style="top:34px">LATEST FROM THE BLOG</h2>
</section>
<article class="post" style="left:99px;top:2179px">
  <div class="pic img" style="left:0;background:linear-gradient(135deg,#e1b98c,#8a6a4c)" role="img" aria-label="Woman in sunglasses at sunset"></div>
  <div class="body" style="left:286px"><h4>Sweet Samantha<br>in sunset on 2015</h4><p class="meta">In: <span>Picturely, Moments</span><br>March 9, 2015 by <span>Ivo Marlen</span></p><span class="more">CONTINUE READING</span></div>
</article>
<article class="post" style="left:612px;top:2179px">
  <div class="body" style="left:28px;text-align:center"><h4>Brand new<br>selection of fashion</h4><p class="meta">In: <span>Picturely, Moments</span><br>March 11, 2015 by <span>Ivo Marlen</span></p><span class="more">CONTINUE READING</span></div>
  <div class="pic img" style="left:234px;background:linear-gradient(135deg,#b9aa96,#4b4038)" role="img" aria-label="Bearded man in a fashion shop"></div>
</article>
<article class="post" style="left:99px;top:2397px">
  <div class="pic img" style="left:0;background:linear-gradient(135deg,#7e9a62,#3f5533)" role="img" aria-label="Woman walking along a tree lined path"></div>
  <div class="body" style="left:286px"><h4>My first trip to<br>New York</h4><p class="meta">In: <span>Picturely, Moments</span><br>April 3, 2015 by <span>Ivo Marlen</span></p><span class="more">CONTINUE READING</span></div>
</article>
<article class="post" style="left:612px;top:2397px">
  <div class="body" style="left:28px;text-align:center"><h4>New breakfast cafe<br>opens today</h4><p class="meta">In: <span>Picturely, Moments</span><br>March 25, 2015 by <span>Ivo Marlen</span></p><span class="more">CONTINUE READING</span></div>
  <div class="pic img" style="left:234px;background:linear-gradient(135deg,#c89a72,#6e4a35)" role="img" aria-label="Breakfast plates on a cafe table"></div>
</article>
<div class="dots" style="left:566px;top:2631px"><span></span><span></span><span class="on"></span><span></span></div>

<div class="partner-logo"><span class="brand-mark"></span><span class="brand-name">HAG</span></div>
<div class="partner-tag">Harbourline Advisory Group</div>
<div class="client" style="left:82px;top:2970px">REDBROOK</div>
<div class="client" style="left:303px;top:2970px">NORVANE</div>
<div class="client" style="left:532px;top:2970px">KELDOR</div>
<div class="client" style="left:759px;top:2970px">ALTURA</div>
<div class="client" style="left:949px;top:2970px">GOLDARCH</div>
<div class="client" style="left:82px;top:3101px">VERONA TIME</div>
<div class="client" style="left:303px;top:3101px">SOLVANI</div>
<div class="client" style="left:532px;top:3101px">HEARTHWAY</div>
<div class="client" style="left:759px;top:3101px">ORBITEK</div>
<div class="client" style="left:949px;top:3101px">PAYLANCE</div>
<div class="dots" style="left:566px;top:3232px"><span></span><span></span><span class="on" style="background:#333;border-color:#333"></span><span></span></div>

<section class="contact" role="img" aria-label="City skyline in a blue tint">
  <h2 class="sec-title" style="top:50px">GET IN TOUCH</h2>
</section>
<h3 class="contact-h3" style="left:99px;top:3440px">We'd Love to Hear From You, Get In Touch With Us!</h3>
<p class="contact-p">At vero eos et accusamus et iusto odio dignissimos ducimus qui blanditiis praesentium voluptatum deleniti atque corrupti quos dolores et quas molestias excepturi sint occaecati cupiditate non provident, similique sunt in culpa qui officia deserunt mollitia animi, id est laborum et dolorum fuga. Et harum quidem rerum facilis est et expedita distinctio nam libero tempore.</p>
<div class="field" style="left:99px;top:3574px;width:226px">Name (required)</div>
<div class="field" style="left:357px;top:3574px;width:231px">Email (required)</div>
<div class="field" style="left:614px;top:3574px;width:231px">Website</div>
<div class="field" style="left:99px;top:3618px;width:746px;height:149px">Comment...</div>

<h3 class="contact-h3" style="left:872px;top:3440px">Contact Info</h3>
<div class="rule" style="top:3465px"></div>
<div class="info">Place Your Address:<br>Telephone:<br>Fax:<br>Email:</div>
<h3 class="contact-h3" style="left:872px;top:3644px">Get Social</h3>
<div class="rule" style="top:3669px"></div>
<div class="social-grid">
  <span></span><span></span><span></span><span></span><span></span><span></span><span></span>
  <span></span><span></span><span></span><span></span><span></span><span></span><span></span>
  <span></span><span></span>
</div>
<div class="footer-line"></div>
<div class="copyright">Copyright 2015 | All Rights Reserved | Powered by Copperleaf</div>

</body>
</html>
```